Business Card Design

Consultation for design, construction athletic facilities specializing in synthetic turf systems and all weather running track systems.
Motto "Plain Client Stewardship"
New Company that we'd like to highlight the LOGO first and foremost with the colors of the background and font as primary colors of the card too if possible. I've also attached a typical larger project design layout that could be used in the background to highlight our design and construction specialty.
Website is something we want very noticeable for driving traffic.
Target Market(s)
Athletic Directors, Designers, Government and Military, Contractors
Industry/Entity Type
Construction
Contact Information for Business Card
Peter K. Halvorsen CPM, CSM
48213 W 37th Ave
Cedar Falls, OR 97431
C +1 555.214.7730
O +1 555.381.4062
Peter@fieldlanepro.com
www.fieldlanepro.com
Look and feel
Each slider illustrates characteristics of the customer's brand and the style your logo design should communicate.

```html
<!DOCTYPE html>
<html lang="en">
<head>
<meta charset="utf-8">
<title>Halden Sport – Business Card</title>
<link rel="stylesheet" href="https://fonts.googleapis.com/css2?family=Roboto:wght@400;700&display=swap">
<style>
  :root {
    --page-bg: #e2e2e2;
    --card-dark: #0b0b0b;
    --card-mid: #1c1c1c;
    --copper: #c9834f;
    --orange: #d98a2b;
    --text-light: #e9e9e9;
    --text-muted: #a3a3a3;
    --rule-light: #d8d8d8;
    --card-edge: #bdbdbd;
  }
  * { box-sizing: border-box; margin: 0; padding: 0; }
  html, body {
    width: 1200px; height: 750px; overflow: hidden;
    background: var(--page-bg);
    font-family: "Roboto", Arial, sans-serif;
  }
  .canvas { position: relative; width: 1200px; height: 750px; }
  .card {
    position: absolute; top: 220px;
    width: 540px; height: 309px;
    border-radius: 30px;
    background: radial-gradient(ellipse at 35% 40%, var(--card-mid) 0%, var(--card-dark) 70%);
    box-shadow: 0 3px 0 var(--card-edge), 0 12px 24px rgba(0,0,0,0.25);
    overflow: hidden;
  }
  .card--front { left: 40px; }
  .card--back { left: 620px; }

  .brand {
    position: absolute; display: flex; align-items: center;
    color: var(--copper); font-weight: 400; white-space: nowrap;
  }
  .brand__dot { border-radius: 50%; background: var(--orange); flex: none; }
  .card--front .brand { left: 0; right: 0; top: 128px; justify-content: center; gap: 18px; }
  .card--front .brand__dot { width: 40px; height: 40px; }
  .card--front .brand__name { font-size: 40px; letter-spacing: 5px; }

  .card--back .brand { left: 40px; top: 96px; gap: 12px; }
  .card--back .brand__dot { width: 26px; height: 26px; }
  .card--back .brand__name { font-size: 26px; letter-spacing: 3px; }

  .rule { position: absolute; height: 1px; }
  .rule--light { background: var(--rule-light); }
  .rule--accent { background: var(--orange); }
  .rule--divider { left: 36px; right: 36px; top: 143px; }
  .rule--address { left: 300px; right: 36px; top: 212px; }
  .rule--motto { left: 240px; right: 36px; top: 270px; }

  .person__name {
    position: absolute; right: 36px; top: 116px;
    color: var(--orange); font-weight: 700; font-size: 16px; white-space: nowrap;
  }
  .person__credential {
    position: absolute; right: 36px; top: 148px;
    color: var(--text-muted); font-size: 10px;
  }
  .address {
    position: absolute; right: 36px; top: 172px; text-align: right;
    color: var(--text-light); font-size: 12px; line-height: 17px;
  }
  .contact {
    position: absolute; left: 36px; top: 166px;
    list-style: none; color: var(--text-light); font-size: 12.5px;
  }
  .contact__item { display: flex; align-items: center; gap: 10px; height: 16px; white-space: nowrap; }
  .contact__icon { width: 12px; height: 12px; flex: none; }
  .contact__item--web { font-weight: 700; }
  .motto {
    position: absolute; left: 36px; top: 263px;
    color: var(--orange); font-size: 12px; letter-spacing: 0.5px; white-space: nowrap;
  }
</style>
</head>
<body>
<main class="canvas">

  <section class="card card--front" aria-label="Card front">
    <div class="brand">
      <span class="brand__dot"></span>
      <span class="brand__name">HALDEN SPORT</span>
    </div>
  </section>

  <section class="card card--back" aria-label="Card back">
    <div class="brand">
      <span class="brand__dot"></span>
      <span class="brand__name">HALDEN SPORT</span>
    </div>

    <p class="person__name">Peter K. Halvorsen</p>
    <div class="rule rule--light rule--divider"></div>
    <p class="person__credential">CPM</p>

    <p class="address">CSM 48213 W 37th Ave<br>Cedar Falls, OR 97431</p>
    <div class="rule rule--accent rule--address"></div>

    <ul class="contact">
      <li class="contact__item">
        <svg class="contact__icon" viewBox="0 0 12 12"><rect x="3" y="0.5" width="6" height="11" rx="1.2" fill="none" stroke="#d98a2b" stroke-width="1.2"/><circle cx="6" cy="9.6" r="0.7" fill="#d98a2b"/></svg>
        <span>+1 555.214.7730</span>
      </li>
      <li class="contact__item">
        <svg class="contact__icon" viewBox="0 0 12 12"><path d="M1 4.5 Q6 1 11 4.5 L10 6 L8 5 L8 4 Q6 3.4 4 4 L4 5 L2 6 Z" fill="#d98a2b"/><rect x="2.5" y="6.5" width="7" height="4.5" rx="0.8" fill="#d98a2b"/></svg>
        <span>+1 555.381.4062</span>
      </li>
      <li class="contact__item">
        <svg class="contact__icon" viewBox="0 0 12 12"><rect x="0.5" y="2" width="11" height="8" rx="1" fill="#d98a2b"/><path d="M0.8 2.5 L6 6.5 L11.2 2.5" fill="none" stroke="#0b0b0b" stroke-width="1"/></svg>
        <span>Peter@fieldlanepro.com</span>
      </li>
      <li class="contact__item contact__item--web">
        <svg class="contact__icon" viewBox="0 0 12 12"><circle cx="6" cy="6" r="5.3" fill="#d98a2b"/><path d="M0.8 6 H11.2 M6 0.8 Q3 6 6 11.2 M6 0.8 Q9 6 6 11.2" fill="none" stroke="#0b0b0b" stroke-width="0.8"/></svg>
        <span>www.fieldlanepro.com</span>
      </li>
    </ul>

    <p class="motto">PLAIN CLIENT STEWARDSHIP</p>
    <div class="rule rule--accent rule--motto"></div>
  </section>

</main>
</body>
</html>
```